Design für recycling Tasche
Zielgruppe
INDIVIDUELLE VERPACKUNGS­LÖSUNGEN
Wir gestalten und fertigen Verpackungen für unterschiedlichste Produkte: Von umweltfreundlichen Tragetaschen und eleganten Schachteln bis zu vollumfassenden Verpackungskonzepten. Das Herz unserer Manufaktur sind hochwertige Materialien, funktionelle Designs und unser Auge fürs Detail.
Wer viel Wert auf individuelle Gestaltungsmöglichkeiten und einzigartige Verpackungslösungen legt, ist in unserer Verpackungswelt genau richtig. Wir bringen über 15 Jahre Erfahrung mit und sind auf der ganzen Welt mit kompetenten Produktionspartnern vernetzt.
Bitte lese sie mehr über uns auf:
https://www.valmetrabox.example/
Aufgabenstellung
Wir möchten ein Design für eine nachhaltige Tasche erarbeiten lassen. Hierfür diese Angaben:
Taschenmaterial besteht aus:
100 % recycled PET (R-PET)
Taschenmaterial ist weiss
Design:
2-farbig
Firmenlogo (ValmetraBox) & website URL kann negativ oder einfarbig verwendet werden
Taschenmasse:
Breite: 500 mm x Tiefe: 180mm x Höhe: 400mm
Main message für Betrachter der Tasche:
- I am really recycled
- love our planet and recycle
- In my first life I was a PET bottle
- What really matters for our planet, is what it´s made from
Zusatz : Es steht dem Designer / der Designerin frei, ob Sie diese main messages in das Design aufnimmt oder nicht; oder eigenen verwendet. Auf jeden Fall müssen sie in Englischer Sprache sein. Die message kann aber auch (nur) visuell ausgedrückt werden.
Das Firmenlogo (ValmetraBox) und Firmenwebsite sind dezent in das Design zu integrieren. Es kann auf den beiden Hauptseiten und in den Seitenfalten integriert werden aber nicht am Boden.
www.valmetrabox.example/

```html
<!DOCTYPE html>
<html lang="en">
<head>
<meta charset="utf-8">
<title>ValmetraBox – Recycled Tote Bag Design</title>
<link href="https://fonts.googleapis.com/css2?family=Anton&family=Teko:wght@400&family=Roboto:wght@400&family=Libre+Baskerville&display=swap" rel="stylesheet">
<style>
  :root {
    --bag-green: #23863a;
    --band-dash: #145c25;
    --cut-red: #e0342c;
    --paper: #ffffff;
    --label-ink: #222222;
    --band-text: #ffffff;
  }
  html, body {
    margin: 0;
    padding: 0;
    width: 1200px;
    height: 3000px;
    overflow: hidden;
    background: var(--paper);
  }
  .bag-sheet {
    display: block;
    width: 1200px;
    height: 3000px;
  }
  .side-label {
    font-family: 'Roboto', Arial, sans-serif;
    font-size: 19px;
    fill: var(--label-ink);
  }
  .headline {
    font-family: 'Anton', Impact, sans-serif;
    font-size: 92px;
  }
  .brand-name {
    font-family: 'Libre Baskerville', Georgia, serif;
    font-size: 15px;
    fill: var(--band-text);
  }
  .brand-url {
    font-family: 'Teko', 'Arial Narrow', sans-serif;
    font-size: 12px;
    fill: var(--band-text);
  }
  .claim-big {
    font-family: 'Teko', 'Arial Narrow', sans-serif;
    font-size: 48px;
    fill: var(--band-text);
  }
  .claim-small {
    font-family: 'Teko', 'Arial Narrow', sans-serif;
    font-size: 31px;
    fill: var(--band-text);
  }
  .band { fill: var(--bag-green); }
  .band-stitch { stroke: var(--band-dash); stroke-width: 1; stroke-dasharray: 4 3; fill: none; }
  .photo-ring { fill: var(--paper); stroke: var(--bag-green); stroke-width: 3; }
  .cut-line { fill: none; stroke: var(--cut-red); stroke-width: 1.2; }
  .fold-line { fill: none; stroke: var(--cut-red); stroke-width: 1; stroke-dasharray: 8 6; }
  .handle-strap { fill: var(--bag-green); }
</style>
</head>
<body>
<svg class="bag-sheet" viewBox="0 0 1030 2575" xmlns="http://www.w3.org/2000/svg">
  <defs>
    <linearGradient id="forest-letters" x1="0" y1="0" x2="1" y2="1">
      <stop offset="0" stop-color="#2f7a2a"/>
      <stop offset="0.35" stop-color="#4f9a3a"/>
      <stop offset="0.55" stop-color="#8aa08a"/>
      <stop offset="0.75" stop-color="#3e8a30"/>
      <stop offset="1" stop-color="#1f5e1e"/>
    </linearGradient>
    <linearGradient id="wildlife-letters" x1="0" y1="0" x2="1" y2="1">
      <stop offset="0" stop-color="#3d8a2f"/>
      <stop offset="0.3" stop-color="#b58a55"/>
      <stop offset="0.55" stop-color="#c9a274"/>
      <stop offset="0.8" stop-color="#9a6a3a"/>
      <stop offset="1" stop-color="#4a7a2c"/>
    </linearGradient>
    <radialGradient id="seedling-photo" cx="0.5" cy="0.5" r="0.6">
      <stop offset="0" stop-color="#7aa04a"/>
      <stop offset="0.35" stop-color="#d9b9a0"/>
      <stop offset="0.7" stop-color="#4a3a30"/>
      <stop offset="1" stop-color="#2a211c"/>
    </radialGradient>
    <linearGradient id="heart-tree-photo" x1="0" y1="0" x2="0" y2="1">
      <stop offset="0" stop-color="#a9cce8"/>
      <stop offset="0.25" stop-color="#5fa33a"/>
      <stop offset="0.6" stop-color="#3f8a26"/>
      <stop offset="1" stop-color="#6fb83a"/>
    </linearGradient>

    <g id="face-care">
      <text class="headline" x="0" y="-159" text-anchor="middle" textLength="308" lengthAdjust="spacingAndGlyphs" fill="url(#forest-letters)" stroke="#1f6b25" stroke-width="1">TAKE CARE</text>
      <text class="headline" x="0" y="-85" text-anchor="middle" textLength="308" lengthAdjust="spacingAndGlyphs" fill="url(#forest-letters)" stroke="#1f6b25" stroke-width="1">OF NATURE</text>
      <rect class="band" x="-215" y="-47" width="430" height="88"/>
      <line class="band-stitch" x1="-213" y1="-42" x2="213" y2="-42"/>
      <line class="band-stitch" x1="-213" y1="36" x2="213" y2="36"/>
      <text class="brand-name" x="-143" y="4" text-anchor="middle">ValmetraBox</text>
      <text class="brand-url" x="-143" y="24" text-anchor="middle">www.valmetrabox.example/</text>
      <text class="claim-big" x="136" y="2" text-anchor="middle">100 %</text>
      <text class="claim-small" x="136" y="26" text-anchor="middle">recycled</text>
      <circle class="photo-ring" cx="0" cy="0" r="73"/>
      <circle cx="0" cy="0" r="67" fill="url(#seedling-photo)" role="img" aria-label="Photo: two cupped hands holding a young green seedling in dark soil"/>
    </g>

    <g id="face-live">
      <text class="headline" x="0" y="-159" text-anchor="middle" textLength="280" lengthAdjust="spacingAndGlyphs" fill="url(#wildlife-letters)" stroke="#1f6b25" stroke-width="1">AND THEY</text>
      <text class="headline" x="0" y="-85" text-anchor="middle" textLength="276" lengthAdjust="spacingAndGlyphs" fill="url(#wildlife-letters)" stroke="#1f6b25" stroke-width="1">WILL LIVE</text>
      <rect class="band" x="-215" y="-47" width="430" height="88"/>
      <line class="band-stitch" x1="-213" y1="-42" x2="213" y2="-42"/>
      <line class="band-stitch" x1="-213" y1="36" x2="213" y2="36"/>
      <text class="brand-name" x="-143" y="4" text-anchor="middle">ValmetraBox</text>
      <text class="brand-url" x="-143" y="24" text-anchor="middle">www.valmetrabox.example/</text>
      <text class="claim-big" x="136" y="2" text-anchor="middle">100 %</text>
      <text class="claim-small" x="136" y="26" text-anchor="middle">recycled</text>
      <circle class="photo-ring" cx="0" cy="0" r="73"/>
      <circle cx="0" cy="0" r="67" fill="url(#heart-tree-photo)" role="img" aria-label="Photo: heart-shaped green tree on a meadow under a blue sky"/>
    </g>

    <g id="gusset-outline">
      <rect class="cut-line" x="0" y="0" width="176" height="419"/>
      <line class="cut-line" x1="0" y1="29" x2="176" y2="29"/>
      <line class="fold-line" x1="12" y1="52" x2="164" y2="52"/>
      <line class="cut-line" x1="6" y1="29" x2="6" y2="413"/>
      <line class="cut-line" x1="170" y1="29" x2="170" y2="413"/>
      <line class="fold-line" x1="11" y1="34" x2="11" y2="408"/>
      <line class="fold-line" x1="165" y1="34" x2="165" y2="408"/>
      <line class="cut-line" x1="6" y1="413" x2="170" y2="413"/>
      <line class="fold-line" x1="11" y1="408" x2="165" y2="408"/>
      <line class="cut-line" x1="0" y1="419" x2="6" y2="413"/>
      <line class="cut-line" x1="176" y1="419" x2="170" y2="413"/>
    </g>

    <g id="handle-loop">
      <path class="handle-strap" d="M408 1180 L442 1180 L442 1355 L408 1355 Z"/>
      <path class="handle-strap" d="M588 1180 L622 1180 L622 1355 L588 1355 Z"/>
      <path class="handle-strap" d="M440 1147 L590 1147 L590 1180 L440 1180 Z"/>
      <path class="cut-line" d="M408 1355 L408 1180 L440 1147 L590 1147 L622 1180 L622 1355"/>
      <path class="cut-line" d="M408 1180 L442 1180 L442 1355 M622 1180 L588 1180 L588 1355"/>
    </g>

    <g id="handle-mark">
      <rect class="cut-line" x="-12" y="-8" width="24" height="16"/>
      <path class="cut-line" d="M-8 -6 L6 0 L-8 6"/>
    </g>
  </defs>

  <!-- flat panels, both bag sides -->
  <text class="side-label" x="278" y="26" text-anchor="middle">1side</text>
  <text class="side-label" x="732" y="26" text-anchor="middle">2side</text>
  <use href="#face-care" transform="translate(277 297)"/>
  <use href="#face-live" transform="translate(735 297)"/>

  <!-- dieline -->
  <use href="#handle-loop"/>
  <use href="#handle-loop" transform="translate(0 3723) scale(1 -1)"/>

  <use href="#gusset-outline" transform="translate(22 1356)"/>
  <use href="#gusset-outline" transform="translate(836 1356)"/>

  <g class="main-panel">
    <rect class="cut-line" x="272" y="1356" width="486" height="1012"/>
    <line class="cut-line" x1="272" y1="1385" x2="758" y2="1385"/>
    <line class="fold-line" x1="284" y1="1408" x2="746" y2="1408"/>
    <line class="cut-line" x1="272" y1="2338" x2="758" y2="2338"/>
    <line class="fold-line" x1="284" y1="2315" x2="746" y2="2315"/>
    <line class="cut-line" x1="281" y1="1385" x2="281" y2="2338"/>
    <line class="cut-line" x1="750" y1="1385" x2="750" y2="2338"/>
    <line class="fold-line" x1="277" y1="1390" x2="277" y2="2333"/>
    <line class="fold-line" x1="754" y1="1390" x2="754" y2="2333"/>
    <line class="cut-line" x1="281" y1="1775" x2="750" y2="1775"/>
    <line class="cut-line" x1="281" y1="1950" x2="750" y2="1950"/>
    <use href="#handle-mark" transform="translate(425 1398)"/>
    <use href="#handle-mark" transform="translate(605 1398)"/>
    <use href="#handle-mark" transform="translate(425 2325) rotate(180)"/>
    <use href="#handle-mark" transform="translate(605 2325) rotate(180)"/>
  </g>

  <use href="#face-care" transform="translate(517 1678) scale(1.13)"/>
  <use href="#face-live" transform="rotate(180 513.5 1861.5) translate(517 1678) scale(1.13)"/>
</svg>
</body>
</html>
```